Warranty Card Design for Mattress Brand

We would like to design a warranty card for our mattresses,
it consists of 2 pages in one card (front and back) to be neatly showing our warranty details/text , our logo , our website, address and telephone clearly.

Target Market(s)

household

Font styles to use
Serif
Script

Colors
3277b5
33a6d7
85cae6
0492cd
3176b5
0355a3
85abd2
cee9f5
85acd3

Requirements
Must have
• a nice warranty logo
Nice to have
• a nice warranty logo with a neat text and clear layout, colors have to be related to the logo

```html
<!DOCTYPE html>
<html lang="en">
<head>
<meta charset="utf-8">
<title>Dreamrest Warranty Card</title>
<link href="https://fonts.googleapis.com/css2?family=Arimo:wght@400;700&family=Cormorant+Garamond:wght@400&display=swap" rel="stylesheet">
<style>
  :root {
    --stage: #a9a9ab;
    --night-deep: #0a1a55;
    --night-mid: #17398f;
    --night-light: #2a5db3;
    --ink-navy: #1c3c8c;
    --ink-blue: #1f4fb0;
    --logo-blue: #3176b5;
    --paper: #ffffff;
    --white: #ffffff;
  }
  * { box-sizing: border-box; margin: 0; padding: 0; }
  html, body { width: 1200px; height: 1013px; overflow: hidden; }
  body {
    background: var(--stage);
    font-family: "Arimo", Arial, sans-serif;
    position: relative;
  }
  .card {
    position: absolute;
    width: 968px;
    height: 435px;
    overflow: hidden;
    box-shadow: 2px 3px 6px rgba(0,0,0,0.35);
  }
  .night-sky {
    position: absolute;
    background: radial-gradient(ellipse at 60% 40%, var(--night-light) 0%, var(--night-mid) 45%, var(--night-deep) 100%);
  }

  /* Front card */
  .card--front { left: 32px; top: 45px; background: var(--night-mid); }
  .card--front .night-sky { left: 0; top: 0; width: 100%; height: 100%; }
  .front-title-band {
    position: absolute; left: 0; top: 35px; width: 100%; height: 59px;
    background: var(--paper);
  }
  .front-title {
    position: absolute; left: 389px; top: 17px;
    font-size: 19px; font-weight: 700; color: var(--ink-navy);
    letter-spacing: 0.1px;
  }
  .brand-frame {
    position: absolute; left: 56px; top: 123px; width: 256px; height: 256px;
    border: 3px solid var(--white);
    display: flex; flex-direction: column; align-items: center; justify-content: center;
  }
  .brand-name {
    font-family: "Arimo", Arial, sans-serif;
    font-size: 42px; font-weight: 400; color: var(--white);
    letter-spacing: 1px; line-height: 1;
  }
  .brand-tagline {
    margin-top: 8px; font-family: "Cormorant Garamond", Georgia, serif;
    font-size: 11px; letter-spacing: 2.5px; color: var(--white);
  }
  .defect-list {
    position: absolute; left: 387px; top: 110px; width: 560px;
    color: var(--white); font-size: 12.4px; line-height: 15.2px;
  }
  .defect-list .indent { padding-left: 10px; }

  /* Back card */
  .card--back { left: 200px; top: 509px; background: var(--paper); }
  .card--back .night-sky { left: 0; top: 0; width: 100%; height: 80px; }
  .back-title {
    position: absolute; left: 34px; top: 44px;
    font-size: 22px; color: var(--white); font-weight: 400;
  }
  .back-copy {
    position: absolute; left: 34px; width: 900px;
    color: var(--ink-blue); font-size: 12px; line-height: 14.7px;
  }
  .back-copy--intro { top: 94px; }
  .back-copy--care { top: 186px; }
  .record-fields {
    position: absolute; top: 292px; left: 34px; width: 600px;
    color: var(--ink-blue); font-size: 12px;
  }
  .record-fields span { position: absolute; top: 0; white-space: nowrap; }
  .dealer-contact {
    position: absolute; left: 34px; top: 358px;
    color: var(--ink-blue); font-size: 12px; line-height: 14.7px;
  }
  .back-brand {
    position: absolute; left: 640px; top: 318px; width: 200px; text-align: center;
  }
  .back-brand .brand-name { color: var(--logo-blue); font-size: 40px; }
  .back-brand .brand-tagline { color: var(--logo-blue); margin-top: 6px; }
</style>
</head>
<body>

<section class="card card--front">
  <div class="night-sky" role="img" aria-label="Deep blue starry night sky backdrop"></div>
  <div class="front-title-band">
    <h2 class="front-title">This limited Mattress Warranty applies to the following Defects:</h2>
  </div>
  <div class="brand-frame">
    <div class="brand-name">dreamrest</div>
    <div class="brand-tagline">MATTRESSES &amp; PILLOWS</div>
  </div>
  <div class="defect-list">
    <div>- Coils or wires that are broken or piercing through fabric.</div>
    <div>- Sagging, that measures 3cm or greater (being properly measured) only if the</div>
    <div class="indent">mattress has been continuously supported by appropriate and solid foundation</div>
    <div>This limited Mattress Warranty does not cover the following:</div>
    <div>- Comfort preference</div>
    <div>- Fabric Stains, soiling or burns</div>
    <div>- Body impressions of less than 3cm</div>
    <div>- Damage to the mattress due to abuse</div>
    <div>- Bent Perimeter border rods due to moving or bending the mattress</div>
    <div>- Size allowance of +/- 2cm</div>
    <div>- Bed Bugs and Dust Mites</div>
    <div>- Mattress Odor: as in any upholstery, new mattress may have odor that will fade with</div>
    <div class="indent">time</div>
    <div>- For Latex and Memory Foam mattresses: normal change in softness and recovery</div>
    <div class="indent">time in these materials with time. This does not affect the relieving qualities of</div>
    <div class="indent">these mattresses.</div>
    <div>- Transportation and Inspection Costs</div>
  </div>
</section>

<section class="card card--back">
  <div class="night-sky" role="img" aria-label="Deep blue starry night sky band"></div>
  <h1 class="back-title">Congratulations on your new DREAMREST mattress.</h1>
  <div class="back-copy back-copy--intro">
    <div>We always strive to provide you with the most comfortable and healthy sleep by offering you the highest product quality and durability.</div>
    <div>Our company was awarded the ISO 9001 accreditation certificate for the quality of its Mattress Production.</div>
    <div>By implementing the ISO 9001 quality management system, we assure our customers that the products and the services we provide will meet their expectations.</div>
    <div>Our products are guaranteed against defects in workmanship and material. In case of defect, we shall repair or replace, at our discretion, the defective component.</div>
    <div>Please keep this card in a safe place. Should you face any problems, please contact our service department</div>
  </div>
  <div class="back-copy back-copy--care">
    <div>To ensure you get maximum comfort and support, please follow the following instructions:</div>
    <div>- Make sure the bed base foundation is in good condition and well ventilated.</div>
    <div>- Turn/Flip your mattress every 3 months to maximize its comfort and lifespan.</div>
    <div>- Avoid exposing the mattress to the sun; air it in a passage area instead.</div>
    <div>- In case of possibility of liquids dripping on the mattress, consider covering it with a mattress protection pad.</div>
    <div>- Do not worry if the mattress feels slightly firmer than anticipated within weeks of usage, the interior will soften and initial stiffness will be removed.</div>
  </div>
  <div class="record-fields">
    <span style="left:0">Invoice Number</span>
    <span style="left:179px">Warranty Period</span>
    <span style="left:379px">Date</span>
  </div>
  <address class="dealer-contact" style="font-style:normal">
    <div>Hadi Saleh and Sons</div>
    <div>Palm Street, Industrial Zone, Northvale</div>
    <div>+961 1 555 014</div>
    <div>www.hadisalehandsons.com</div>
  </address>
  <div class="back-brand">
    <div class="brand-name">dreamrest</div>
    <div class="brand-tagline">MATTRESSES &amp; PILLOWS</div>
  </div>
</section>

</body>
</html>
```